NEW Wordpress Website Design for a Dynamic Long Term Healthcare Company in Hawaii

I would like a new website design for my current company, Marlow Haven Partners, which has two different brands - Marlow Homecare and Marlow Senior Living. You can see the current website at www.marlowhaven.example. The website should be built using Wordpress Software and the Elementor theme. The website should have a local Hawaii island/tropical feel, but look professional for healthcare. I'm looking for something fresh, and want the designer to select colors, styles, etc.

In the Header, on all pages, I would like a menu that includes Home Care, Senior Living, Rates, and About Us.
Under each of the Header Menu Titles, I would like these drop downs included:
Home Care (drop down pages)- Nurse Aide Care, 24-Hour Home Care, Skilled Nursing, Lifestyle Aide, Hospice at Home, Bathing & Meal Service.
Senior Living (drop down pages) - Long-Term Stay, Short-Term Stay.
Rates (drop down page) - Rates.
About Us (drop down pages) - Our Mission, Ohana Talk, About Doreen Marlow.

In the footer, on all pages, you should include the address: 248 Lanakila Ave, Suite 310, Honolulu, HI 96817. Phone number: 808-555-0173
The footer should also include buttons for a page called Learn, Caregiver Jobs, and each of the service page links to include: Nurse Aide Care, 24-Hour Home Care, Skilled Nursing, Lifestyle Aide, Hospice at Home, Bathing & Meal Service.
Please don't take the current website and redesign a few aspects. I'm looking for a completely different look and feel.

Target Market(s)

40-80 year olds

Industry/Entity Type

Long Term Healthcare

Coding

Coded - Design and coding required

Requirements
Should not have
• Our existing website as a template. We are looking for a complete redesign. Thank you.

```html
<!DOCTYPE html>
<html lang="en">
<head>
<meta charset="utf-8">
<title>Marlow Haven Partners – Mobile Website Screens</title>
<link rel="stylesheet" href="https://fonts.googleapis.com/css2?family=Poppins:wght@400;500;600;700&family=Open+Sans:wght@400;700;800&display=swap">
<style>
:root{
  --coral:#f6837a;
  --coral-soft:#fde3e6;
  --ink:#262626;
  --muted:#8d8d8d;
  --line:#ececec;
  --paper:#ffffff;
  --stage:#f3f3f4;
  --teal:#4f9a9c;
}
*{box-sizing:border-box;margin:0;padding:0}
html,body{width:1200px;height:1200px;overflow:hidden;background:var(--stage)}
body{position:relative;font-family:"Poppins",sans-serif;color:var(--ink)}

.brand-row{position:absolute;left:40px;top:40px;display:flex;gap:34px;align-items:center}
.brand{display:flex;align-items:center;gap:8px;font-size:20px;font-weight:600}
.brand .mark{width:20px;height:20px;border-radius:4px}
.brand--home{color:var(--coral)} .brand--home .mark{background:var(--coral)}
.brand--group{color:var(--ink)} .brand--group .mark{background:var(--ink)}
.brand--senior{color:var(--teal)} .brand--senior .mark{background:var(--teal)}

.screen{position:absolute;width:270px;background:var(--paper);border-radius:22px;padding:22px;box-shadow:0 18px 40px rgba(0,0,0,.07);overflow:hidden}
.eyebrow{color:var(--coral);font-size:11px;margin-bottom:4px}
.title{font-size:20px;font-weight:600;line-height:1.25;margin-bottom:12px}
.body{font-size:10px;color:var(--muted);line-height:1.7}
.btn-outline{display:inline-flex;align-items:center;gap:6px;border:1px solid var(--coral);color:var(--coral);border-radius:22px;padding:9px 26px;font-size:11px;margin-top:16px}
.photo{border-radius:16px;margin-top:16px}

/* services */
.service-list{position:relative;margin-top:6px;padding-left:12px;border-left:3px solid var(--line)}
.service-list::before{content:"";position:absolute;left:-3px;top:0;height:48%;width:3px;background:var(--coral)}
.service{padding:14px 12px}
.service h4{font-size:12px;font-weight:600;margin-bottom:3px}
.service p{font-size:9px;color:var(--muted)}
.service--active{box-shadow:0 6px 20px rgba(0,0,0,.07);border-radius:12px}
.service--active h4{color:var(--coral);display:flex;align-items:center;gap:8px}
.badge{width:22px;height:22px;border-radius:50%;background:var(--coral);color:#fff;font-size:9px;display:grid;place-items:center}

/* hero */
.hero-screen{padding:0}
.topbar{display:flex;justify-content:space-between;align-items:center;padding:14px 18px}
.topbar .brand{font-size:12px}
.burger{width:18px;display:grid;gap:4px}
.burger span{height:2px;background:var(--coral)}
.hero{position:relative;height:420px;background:linear-gradient(160deg,#c9b35a 0%,#9a6a3c 40%,#5a4a3c 75%,#3c3a44 100%);padding:26px 20px}
.hero h1{font-family:"Open Sans",sans-serif;font-weight:800;color:#fff;font-size:22px;line-height:1.3;letter-spacing:.5px}
.hero p{color:#fff;font-size:10px;line-height:1.7;margin-top:14px;opacity:.95}
.btn-solid{display:inline-block;background:var(--coral);color:#fff;border-radius:24px;padding:12px 40px;font-size:12px;margin-top:22px}
.hero-foot{padding:16px 20px}

/* pricing cards */
.price-card{position:absolute;width:270px;background:var(--coral);border-radius:22px;padding:26px 24px;color:#fff}
.price-card .plan{text-align:center;font-size:12px}
.price-card .price{text-align:center;font-size:32px;font-weight:700;margin:8px 0}
.price-card .desc{text-align:center;font-size:10px;line-height:1.6;margin-bottom:14px}
.checks{list-style:none;display:grid;gap:9px}
.checks li{display:flex;align-items:center;gap:10px;font-size:11px}
.btn-white{display:block;text-align:center;background:#fff;color:var(--ink);border-radius:14px;padding:13px;font-size:12px;margin-top:20px}

/* rates */
.tabs{display:flex;gap:8px;margin-top:14px}
.tabs span{flex:1;font-size:9px;padding:10px;border-radius:8px;background:#f5f5f5;color:var(--muted);text-align:center}
.tabs .on{background:var(--coral-soft);color:var(--coral)}
.rate-bar{height:40px;background:var(--coral);border-radius:14px 14px 0 0;margin-top:14px}

/* footer */
.footer-brands{display:flex;gap:14px;margin-bottom:14px}
.footer-brands .brand{font-size:12px}
.footer-brands .mark{width:12px;height:12px}
.footer h5{color:var(--coral);font-size:12px;font-weight:600;margin:10px 0 6px}
.socials{display:flex;gap:8px;padding-bottom:12px;border-bottom:1px solid var(--line)}
.socials span{width:20px;height:20px;border-radius:50%;background:var(--coral)}
.links{list-style:none;display:grid;gap:4px;font-size:10px;color:var(--coral);opacity:.85}
.contact{font-size:9px;color:var(--muted);margin-top:10px;line-height:1.6}
</style>
</head>
<body>

<div class="brand-row">
  <div class="brand brand--home"><span class="mark"></span>Marlow Homecare</div>
  <div class="brand brand--group"><span class="mark"></span>Marlow Haven Partners</div>
  <div class="brand brand--senior"><span class="mark"></span>Marlow Senior Living</div>
</div>

<!-- column 1 -->
<section class="screen" style="left:40px;top:120px">
  <div class="eyebrow">Home care</div>
  <h2 class="title">Our success is a reflection of our experience</h2>
  <div class="service-list">
    <div class="service service--active"><h4><span class="badge">24</span>24-Hour Home Care</h4><p>It has roots in a piece of classical</p></div>
    <div class="service"><h4>Nurse Aide Care</h4><p>It has roots in a piece of classical</p></div>
    <div class="service"><h4>Skilled Nursing</h4><p>It has roots in a piece of classical</p></div>
    <div class="service"><h4>Lifestyle Aid</h4><p>It has roots in a piece of classical</p></div>
  </div>
  <span class="btn-outline">Call today</span>
</section>

<div class="price-card" style="left:40px;top:680px">
  <ul class="checks">
    <li><svg width="14" height="14" viewBox="0 0 14 14"><circle cx="7" cy="7" r="7" fill="#fff"/><path d="M4 7.2l2 2 4-4.4" stroke="#f6837a" stroke-width="1.6" fill="none"/></svg>Lorem ipsum dolor sit</li>
    <li><svg width="14" height="14" viewBox="0 0 14 14"><circle cx="7" cy="7" r="7" fill="#fff"/><path d="M4 7.2l2 2 4-4.4" stroke="#f6837a" stroke-width="1.6" fill="none"/></svg>Dorem ipsum dolor sit</li>
    <li><svg width="14" height="14" viewBox="0 0 14 14"><circle cx="7" cy="7" r="7" fill="#fff"/><path d="M4 7.2l2 2 4-4.4" stroke="#f6837a" stroke-width="1.6" fill="none"/></svg>Yorem ipsum dolor sit</li>
    <li><svg width="14" height="14" viewBox="0 0 14 14"><circle cx="7" cy="7" r="7" fill="#fff"/><path d="M4 7.2l2 2 4-4.4" stroke="#f6837a" stroke-width="1.6" fill="none"/></svg>Worem ipsum dolor sit</li>
    <li><svg width="14" height="14" viewBox="0 0 14 14"><circle cx="7" cy="7" r="7" fill="#fff"/><path d="M4 7.2l2 2 4-4.4" stroke="#f6837a" stroke-width="1.6" fill="none"/></svg>Corem ipsum dolor sit</li>
    <li><svg width="14" height="14" viewBox="0 0 14 14"><circle cx="7" cy="7" r="7" fill="#fff"/><path d="M4 7.2l2 2 4-4.4" stroke="#f6837a" stroke-width="1.6" fill="none"/></svg>Korem ipsum dolor sit</li>
  </ul>
  <span class="btn-white">Call now</span>
</div>

<!-- column 2 -->
<section class="screen hero-screen" style="left:330px;top:120px">
  <div class="topbar"><div class="brand brand--home"><span class="mark" style="width:12px;height:12px"></span>Marlow</div><div class="burger"><span></span><span></span><span></span></div></div>
  <div class="hero" role="img" aria-label="Photo of a caregiver exercising with smiling seniors in a bright living room">
    <h1>HAWAII'S CHOICE HOMECARE &amp; SENIOR LIVING</h1>
    <p>Marlow Homecare provides professional in-home healthcare services throughout the entire island of Oahu. Marlow Senior Living, a beautiful Adult Residential Care Home located on the windward side of Oahu in Kailua.</p>
    <span class="btn-solid">Contact us</span>
  </div>
  <div class="hero-foot"><div class="eyebrow">Home care</div><h2 class="title" style="margin:0">Our success is a</h2></div>
</section>

<section class="screen" style="left:330px;top:750px">
  <div class="eyebrow">About Us</div>
  <h2 class="title">About Marlow Haven Partners</h2>
  <p class="body">At Marlow Haven Partners, our mission is to provide compassionate and professional long-term healthcare services that empower individuals to maintain their highest level of independence, health, and well-being in the comfort of their own homes or ours, either through our licensed home healthcare agency - Marlow Homecare, or in our Adult Residential Care Home - Marlow Senior Living.</p>
  <span class="btn-outline">Read more
    <svg width="10" height="10" viewBox="0 0 10 10"><path d="M2 8L8 2M3.5 2H8v4.5" stroke="#f6837a" stroke-width="1.2" fill="none"/></svg></span>
</section>

<!-- column 3 -->
<section class="screen" style="left:630px;top:120px">
  <div class="eyebrow">About Us</div>
  <h2 class="title">About Marlow Haven Partners</h2>
  <p class="body">At Marlow Haven Partners, our mission is to provide compassionate and professional long-term healthcare services that empower individuals to maintain their highest level of independence, health, and well-being in the comfort of their own homes or ours.</p>
  <span class="btn-outline">Read more
    <svg width="10" height="10" viewBox="0 0 10 10"><path d="M2 8L8 2M3.5 2H8v4.5" stroke="#f6837a" stroke-width="1.2" fill="none"/></svg></span>
  <div class="photo" role="img" aria-label="Photo of three women sharing a craft table by sunny windows" style="height:150px;background:linear-gradient(150deg,#e6dc8a,#b58a52 60%,#7a5a3a)"></div>
</section>

<section class="screen" style="left:630px;top:620px">
  <span class="btn-outline" style="margin-top:0">Call today</span>
  <div class="photo" role="img" aria-label="Photo of a caregiver walking beside a resident with a walker in a tropical garden" style="height:170px;background:linear-gradient(160deg,#7fa45a,#4d7a3c 55%,#c9c2b4)"></div>
  <h2 class="title" style="text-align:center;margin-top:16px">Our Rates</h2>
  <p class="body" style="text-align:center">Lorem ipsum dolor sit amet, consectetur adipiscing elit. Nunc vulputate libero et velit interdum, ac aliquet odio mattis.</p>
  <div class="tabs"><span>Homecare Services</span><span class="on">Senior Living</span></div>
  <div class="rate-bar"></div>
</section>

<!-- column 4 -->
<div class="price-card" style="left:920px;top:120px">
  <div class="plan">Senior Living - Short-Term Stay</div>
  <div class="price">$14.50</div>
  <p class="desc">Vorem ipsum dolor sit amet, consectetur adipiscing elit.</p>
  <ul class="checks">
    <li><svg width="14" height="14" viewBox="0 0 14 14"><circle cx="7" cy="7" r="7" fill="#fff"/><path d="M4 7.2l2 2 4-4.4" stroke="#f6837a" stroke-width="1.6" fill="none"/></svg>Jorem ipsum dolor sit</li>
    <li><svg width="14" height="14" viewBox="0 0 14 14"><circle cx="7" cy="7" r="7" fill="#fff"/><path d="M4 7.2l2 2 4-4.4" stroke="#f6837a" stroke-width="1.6" fill="none"/></svg>Dorem ipsum dolor sit</li>
    <li><svg width="14" height="14" viewBox="0 0 14 14"><circle cx="7" cy="7" r="7" fill="#fff"/><path d="M4 7.2l2 2 4-4.4" stroke="#f6837a" stroke-width="1.6" fill="none"/></svg>Worem ipsum dolor sit</li>
    <li><svg width="14" height="14" viewBox="0 0 14 14"><circle cx="7" cy="7" r="7" fill="#fff"/><path d="M4 7.2l2 2 4-4.4" stroke="#f6837a" stroke-width="1.6" fill="none"/></svg>Corem ipsum dolor sit</li>
  </ul>
  <span class="btn-white">Call now</span>
</div>

<footer class="screen footer" style="left:920px;top:560px">
  <div class="footer-brands">
    <div class="brand brand--home"><span class="mark"></span>Marlow</div>
    <div class="brand brand--group"><span class="mark"></span>Marlow</div>
  </div>
  <h5>Get In Touch</h5>
  <div class="socials"><span></span><span></span><span></span></div>
  <h5>Pages</h5>
  <ul class="links"><li>Home</li><li>About</li><li>Service</li><li>Blog</li></ul>
  <h5>Services</h5>
  <ul class="links"><li>Learn</li><li>Caregiver Jobs</li><li>Nurse Aide Care</li><li>24-Hour Home Care</li><li>Skilled Nursing</li><li>Lifestyle Aide</li><li>Hospice At Home</li></ul>
  <p class="contact">248 Lanakila Ave, Suite 310, Honolulu, HI 96817<br>808-555-0173</p>
</footer>

</body>
</html>
```